Tranquil Harbor yoga, meditation & wellness

I teach kundalini yoga and meditation classes.
I have adult beginner classes, seniors classes, family yoga classes, kids yoga classes
I also offer events like cacao ceremony, full moon ceremony, and retreats

Professional, and simple website that is easy to navigate, and easy for me to update, change.

Target Market(s)

all ages

Industry/Entity Type

Health And Wellness

Coding

Coded - Design and coding required

Number of Pages Required

5+ page

Font styles to use
Decorative

Colors
cedeed
eedded
e4daeb
fbd4d5
fee3d4

Requirements
Must have
• tabs required: about, contact, events, classes, blog,
• I would like to link my facebook page & snapfeed accounts to the website
Nice to have
• I would like my clients to be able to register for classes and events from my website
• I would like to have a "shop" option in the future, for some items that I have for sale

```html
<!DOCTYPE html>
<html lang="en">
<head>
<meta charset="utf-8">
<title>Tranquil Harbor – Kundalini Yoga &amp; Meditation</title>
<link rel="stylesheet" href="https://fonts.googleapis.com/css2?family=Allura&family=Montserrat:wght@300;400;500;600&display=swap">
<style>
:root{
  --teal:#0aa9bf;
  --teal-deep:#0897ab;
  --aqua:#c6ecf1;
  --aqua-mid:#9fdeea;
  --coral:#f4a19c;
  --ink:#2b2b2b;
  --body:#5a5a5a;
  --white:#ffffff;
  --script:'Allura', cursive;
  --sans:'Montserrat', sans-serif;
}
*{box-sizing:border-box;margin:0;padding:0}
html,body{width:1200px;height:2927px;overflow:hidden}
body{font-family:var(--sans);color:var(--ink);background:var(--aqua);position:relative}
.script{font-family:var(--script);font-weight:400}
.btn{position:absolute;display:flex;align-items:center;justify-content:center;border-radius:16px;color:var(--white);font-size:11px;font-weight:500;font-family:var(--sans);white-space:nowrap}
.btn-teal{background:var(--teal)}
.btn-coral{background:var(--coral)}

/* header + hero */
.hero{position:absolute;left:0;top:0;width:1200px;height:599px;background:linear-gradient(180deg,#e9edf0 0%,#f4f6f7 45%,#e6eaed 100%)}
.hero-photo{position:absolute;left:640px;top:80px;width:380px;height:519px;background:linear-gradient(180deg,rgba(236,236,238,0) 0%,#ece6e4 18%,#efeceb 55%,rgba(230,234,237,0) 100%)}
.brand{position:absolute;left:38px;top:22px;display:flex;align-items:center;gap:8px}
.brand-dot{width:13px;height:13px;border-radius:50%;background:var(--coral)}
.brand-name{font-family:var(--script);font-size:31px;color:#4a4a4a;line-height:1;white-space:nowrap}
.brand-sub{position:absolute;left:68px;top:56px;font-size:11px;color:#6a6a6a;letter-spacing:.5px;white-space:nowrap}
.nav{position:absolute;top:44px;left:360px;display:flex;gap:26px;font-size:11px;font-weight:500;color:#444;white-space:nowrap}
.nav .active{color:var(--teal)}
.nav .call{color:var(--coral)}
.register-label{position:absolute;left:812px;top:38px;font-family:var(--script);font-size:20px;color:#555;white-space:nowrap}
.hero-kicker{position:absolute;left:152px;top:232px;font-size:27px;color:var(--teal);white-space:nowrap}
.hero-title{position:absolute;left:152px;top:270px;font-size:45px;font-weight:300;line-height:1.2;color:#222;width:540px}

/* about */
.photo{position:absolute}
.ph-a{left:150px;top:599px;width:301px;height:300px;background:linear-gradient(135deg,#c9b9aa,#efe7df 55%,#a48774)}
.ph-b{left:451px;top:599px;width:299px;height:599px;background:linear-gradient(160deg,#eeeae6 0%,#d9c2b2 45%,#8a7a70 80%,#5e5a58)}
.ph-c{left:451px;top:1198px;width:599px;height:600px;background:linear-gradient(150deg,#c7b8ad 0%,#ece6e1 40%,#d2bfb2 70%,#b8a79c)}
.teacher-name{position:absolute;left:150px;top:920px;font-size:48px;color:#333;line-height:1}
.teacher-alt{position:absolute;left:152px;top:968px;font-size:26px;color:var(--teal);white-space:nowrap}
.teacher-role{position:absolute;left:152px;top:1010px;font-size:10px;color:#444}
.rule{position:absolute;height:1px;width:72px;background:#9fc9d0}
.teacher-bio{position:absolute;left:152px;top:1064px;width:226px;font-size:11px;line-height:1.72;color:var(--body);text-align:justify;hyphens:auto}
.teacher-bio p{margin-bottom:18px}
.intro-kicker{position:absolute;left:825px;top:630px;font-size:24px;color:var(--teal);white-space:nowrap}
.intro-title{position:absolute;left:825px;top:674px;font-size:28px;font-weight:400;line-height:1.22;color:#222}
.intro-text{position:absolute;left:825px;top:806px;width:226px;font-size:11px;line-height:1.72;color:var(--body);text-align:justify;hyphens:auto}
.intro-text p{margin-bottom:18px}
.intro-text em{color:var(--teal);font-style:italic}
.card{position:absolute;left:150px;top:1498px;width:601px;height:301px;background:var(--white)}
.card-kicker{position:absolute;left:76px;top:50px;font-size:24px;color:var(--teal);white-space:nowrap}
.card-title{position:absolute;left:76px;top:96px;font-size:27px;font-weight:400;color:#222;white-space:nowrap}
.card-text{position:absolute;left:76px;top:138px;width:490px;font-size:10.5px;line-height:1.6;color:var(--body)}

/* testimonial */
.voices{position:absolute;left:0;top:1799px;width:1200px;height:375px;background:var(--aqua-mid)}
.ornament{position:absolute;left:150px;top:36px;width:300px;height:310px;border-radius:50%;background:radial-gradient(circle,rgba(255,255,255,.28) 0%,rgba(255,255,255,.12) 55%,rgba(255,255,255,0) 72%)}
.voice-photo{position:absolute;left:226px;top:124px;width:148px;height:148px;border-radius:50%;background:linear-gradient(160deg,#c7d9c4,#8a9a80 55%,#5d6a70);border:3px solid var(--white)}
.voices h2{position:absolute;left:525px;top:66px;font-size:27px;font-weight:400;color:#222;white-space:nowrap}
.voices .rule{left:525px;top:112px}
.voices blockquote{position:absolute;left:525px;top:140px;width:520px;font-size:13px;line-height:1.5;color:#666;white-space:nowrap}
.voices cite{position:absolute;left:525px;top:276px;font-size:12px;font-style:normal;font-weight:600;color:#444}
.dots{position:absolute;left:1038px;top:146px;display:flex;flex-direction:column;gap:9px}
.dots span{width:10px;height:10px;border-radius:50%;border:1px solid #5fa8b6}

/* photo feed */
.social{position:absolute;left:0;top:2174px;width:1200px;height:410px;background:var(--aqua)}
.follow{position:absolute;left:0;width:1200px;top:52px;text-align:center;font-size:26px;line-height:1;color:var(--teal)}
.feed-label{position:absolute;left:0;width:1200px;top:82px;display:flex;justify-content:center;align-items:center;gap:7px;font-size:27px;font-weight:300;line-height:1.1;color:#222}
.feed-label i{width:13px;height:13px;background:#222;display:block}
.feed{position:absolute;left:75px;top:146px;display:flex;gap:4px}
.feed div{width:207px;height:204px}
.f1{background:linear-gradient(150deg,#8a8f92,#d8cfc4 60%,#6d6f72)}
.f2{background:linear-gradient(160deg,#c9b8a5,#efe9e3 50%,#5b5855)}
.f3{background:linear-gradient(150deg,#7e7a82,#c9b3a8 55%,#4f4c54)}
.f4{background:linear-gradient(150deg,#b9a89a,#caa187 50%,#6d7a63)}
.f5{background:linear-gradient(150deg,#d8dde0,#8f7766 55%,#e9ecee)}

/* newsletter */
.news{position:absolute;left:0;top:2584px;width:1200px;height:150px;background:var(--teal)}
.news h2{position:absolute;left:151px;top:36px;font-size:46px;color:var(--white);line-height:1;white-space:nowrap}
.news p{position:absolute;left:151px;top:88px;font-size:12px;color:#e6f8fb}
.news-field{position:absolute;left:525px;top:36px;width:527px;height:73px;border-radius:37px;background:var(--teal-deep)}
.news-field span{position:absolute;left:36px;top:29px;font-size:11px;color:var(--white)}
.news-field .btn{left:405px;top:14px;width:108px;height:44px;border-radius:22px}

/* footer */
.footer{position:absolute;left:0;top:2734px;width:1200px;height:193px;background:var(--aqua)}
.footer-icons{position:absolute;left:0;width:1200px;top:58px;display:flex;justify-content:center;gap:13px}
.footer-icons svg{display:block}
.footer small{position:absolute;left:0;width:1200px;top:100px;text-align:center;font-size:10.5px;line-height:1.75;color:#555}
</style>
</head>
<body>

<header class="hero">
  <div class="hero-photo" role="img" aria-label="Photo of the instructor in white clothing and head wrap meditating in a snowy landscape"></div>
  <div class="brand"><span class="brand-dot"></span><span class="brand-name">Tranquil Harbor</span></div>
  <div class="brand-sub">Kundalini Yoga &amp; Meditation</div>
  <nav class="nav">
    <span class="active">About</span><span>Events</span><span>Classes</span><span>Blog</span><span>Contact</span><span class="call">Call +1 204-555-0142</span>
  </nav>
  <div class="register-label">Register for:</div>
  <span class="btn btn-coral" style="left:900px;top:34px;width:91px;height:31px">Classes</span>
  <span class="btn btn-coral" style="left:997px;top:34px;width:91px;height:31px">Events</span>

  <div class="hero-kicker script">Maren (Sat Prem Kaur)</div>
  <h1 class="hero-title">The holistic “yoga of awareness”</h1>
  <span class="btn btn-teal" style="left:150px;top:420px;width:119px;height:31px">Explore More</span>
</header>

<section class="about">
  <div class="photo ph-a" role="img" aria-label="Photo of the instructor seated in white, preparing for practice"></div>
  <div class="photo ph-b" role="img" aria-label="Close-up photo of a hand resting in a meditation mudra on the knee"></div>
  <div class="photo ph-c" role="img" aria-label="Photo of the instructor with raised arms during a kundalini posture"></div>

  <div class="teacher-name script">Maren</div>
  <div class="teacher-alt script">(Sat Prem Kaur)</div>
  <div class="teacher-role">kundalini yoga instructor</div>
  <div class="rule" style="left:152px;top:1034px"></div>
  <div class="teacher-bio">
    <p>I have been practicing yoga for about 5 years, I began practicing Kundalini yoga 2 years ago, and it ignited a complete transformation of mind, body and spirit. I knew that I would go on to teach this lineage.</p>
    <p>I'm also a nurse part time with the RHCA, my 18 years of health care experience has been invaluable.</p>
    <p>My most important job of all is wife, mother and home educator to my four daughters, ages 9-4 years.</p>
  </div>
  <span class="btn btn-teal" style="left:150px;top:1408px;width:119px;height:31px">Read More</span>

  <div class="intro-kicker script">Tranquil Harbor</div>
  <h2 class="intro-title">Kundalini<br>yoga and medi-<br>tation</h2>
  <div class="rule" style="left:825px;top:785px"></div>
  <div class="intro-text">
    <p>Kundalini Yoga comes from northern India and has a centuries-long tradition. It was brought to the West by <em>Yogi Anand Dev</em> in 1968. It is a powerful yoga system that includes not only physical and meditation exercises, but also healing techniques such as <em>Sat Nam Rasayan</em> and yogic massage, nutrition and lifestyle teachings of <em>Ayurveda</em>, and yogic lifestyle.</p>
    <p>The comprehensive science of Kundalini Yoga also includes <em>Numerology</em>, ...</p>
  </div>
  <span class="btn btn-teal" style="left:825px;top:1108px;width:119px;height:31px">Read More</span>

  <div class="card">
    <div class="card-kicker script">Kundalini Yoga -</div>
    <h2 class="card-title">The yoga for everyone</h2>
    <p class="card-text">Kundalini Yoga is therefore suitable for people of all ages and physical condition.<br>Its beneficial effect is quickly noticeable.</p>
    <span class="btn btn-coral" style="left:75px;top:210px;width:165px;height:31px">Register for Classes</span>
  </div>
</section>

<section class="voices">
  <div class="ornament" role="img" aria-label="Soft floral ornament behind the client photo"></div>
  <div class="voice-photo" role="img" aria-label="Round photo of a smiling couple who attended a class"></div>
  <h2>What our people say</h2>
  <div class="rule"></div>
  <blockquote>Such an awesome experience yesterday with Kundalini yoga!<br>Could sense things I didn't even realize were around me.<br>Maren is an incredible instructor and was extremely helpful and<br>thorough in explaining processes, breathing exercises, etc.<br>I would highly recommend trying ...</blockquote>
  <cite>Lorena Vasquez -</cite>
  <div class="dots"><span></span><span></span><span></span><span></span><span></span></div>
</section>

<section class="social">
  <div class="follow script">follow @ <u>theharborhearth</u></div>
  <div class="feed-label"><i></i>snapfeed</div>
  <div class="feed">
    <div class="f1" role="img" aria-label="Feed photo of a child baking in a kitchen"></div>
    <div class="f2" role="img" aria-label="Feed photo of the instructor holding a newborn"></div>
    <div class="f3" role="img" aria-label="Feed photo of children holding a baby"></div>
    <div class="f4" role="img" aria-label="Feed photo of a mother with her daughter outdoors"></div>
    <div class="f5" role="img" aria-label="Feed photo of a family at a festive dinner table"></div>
  </div>
</section>

<section class="news">
  <h2 class="script">Get the updates</h2>
  <p>Join the newsletter and stay up to date with us</p>
  <div class="news-field">
    <span>name@email.com</span>
    <span class="btn btn-coral">Subscribe</span>
  </div>
</section>

<footer class="footer">
  <div class="footer-icons">
    <svg width="19" height="19" viewBox="0 0 19 19" fill="none" stroke="#0aa9bf" stroke-width="1.5" aria-label="Social page link"><rect x="1" y="1" width="17" height="17" rx="2"/></svg>
    <svg width="19" height="19" viewBox="0 0 19 19" fill="none" stroke="#0aa9bf" stroke-width="1.5" aria-label="Photo feed link"><rect x="1" y="1" width="17" height="17" rx="2"/></svg>
    <svg width="19" height="19" viewBox="0 0 19 19" fill="none" stroke="#0aa9bf" stroke-width="1.5" aria-label="Email link"><rect x="1" y="1" width="17" height="17" rx="2"/><path d="M4 6 L9.5 10.5 L15 6 M4 6 H15 V13 H4Z"/></svg>
  </div>
  <small>© 2018 Tranquil Harbor Kundalini Yoga.<br>All Rights Reserved</small>
</footer>

</body>
</html>
```